Jest Harbor Website - Corporate Comedy Show

I've created a company called "Jest Harbor". We put on corporate comedy shows for companies all over the country. I'd like to design a nice, sleek, professional website, similar to Ridora's: https://www.ridora-example.com. We like the one page layout.
Tagline: Your Team's Desk-Grin Ratio
I need the following sections:
1. first section would be scrolling images of the company logo and tagline, with 2 or 3 other scrolling images. Testimonials.
2. The next section below would be an about the company section. a small paragraph describing what we do.
4. The next section below would be for a promo video
5. The next section below would be for bios...my partner and I would have transparent head shots, side by side split-screen. When you hover over our headshots, a button for "bio" appears. When you click the "bio" button, an expanded bio appears.
6. Contact section. Newsletter subscription. A section where people enter their email and short message of what they're linking for that will link directly to our email addresses.
7. Additional content. Scrolling video gallery of our sketch videos. (a section that links to a page with videos and content)
Target Market(s)
Corporate Executives, Event Planners, Event Coordinators, Marketing and HR managers, Venue owners
Industry/Entity Type
It Company
Coding
Coded - Design and coding required
Number of Pages Required
1 page
Font styles to use
Other font styles liked:
- FunctionPro
Requirements
Must have
- -Please use the branded colors from the logo. Burgundy and Blue;
- -A contact section where people put in their email address, company they are from and a small memo to describe the event they're hosting, which will then get sent directly to our email accounts;
- -email accounts that are "marcus@thejestharbor-example.com" and "oliver@thejestharbor-example.com" that link to our zipmail accounts
- -getting our domain linked and hosted and all setup (www.thejestharbor-example.com- bought from SiteBarn)
Nice to have
- Build in Plotly Pages because we are familiar with it and know how to update
Should not have
- basic, generic look. too much white space (but soon is good!)

```html
<!DOCTYPE html>
<html lang="en">
<head>
<meta charset="utf-8">
<title>Jest Harbor</title>
<link href="https://fonts.googleapis.com/css2?family=Jost:wght@400;500&family=Open+Sans:wght@400&display=swap" rel="stylesheet">
<style>
:root{
  --burgundy:#8a1020;
  --ink:#222;
  --body-text:#7a7a7a;
  --rule:#333;
  --white:#fff;
  --stage-dark:#1a0205;
  --stage-mid:#5e080e;
  --stage-bright:#a8141c;
  --photo-light:#cfc3c0;
  --photo-mid:#5d6478;
  --photo-low:#8c8595;
}
*{margin:0;padding:0;box-sizing:border-box}
html,body{width:1200px;height:1000px;overflow:hidden;background:var(--white)}
body{font-family:"Jost",sans-serif;color:var(--ink);position:relative}

.site-header{position:absolute;top:0;left:0;width:1200px;height:118px;border-bottom:3px solid var(--rule);background:var(--white)}
.menu-toggle{position:absolute;left:128px;top:46px;display:flex;align-items:center;gap:12px;font-size:18px;letter-spacing:.5px;color:var(--ink)}
.brand{position:absolute;left:0;width:1200px;top:37px;text-align:center;font-size:32px;line-height:40px;font-weight:400;letter-spacing:1px;color:var(--burgundy);text-transform:uppercase}
.social{position:absolute;right:137px;top:51px;display:flex;gap:9px;list-style:none;font-size:11px;color:var(--burgundy)}

.hero{position:absolute;top:118px;left:0;width:1200px;height:472px;
  background:
    radial-gradient(ellipse at 50% 38%, rgba(190,22,28,.75), transparent 65%),
    linear-gradient(180deg, var(--stage-mid) 0%, var(--stage-bright) 45%, var(--stage-dark) 100%);}
.hero-title{position:absolute;top:178px;left:0;width:1200px;text-align:center;color:var(--white);font-size:54px;line-height:56px;font-weight:400}
.hero-title strong{font-weight:500}
.slide-arrow{position:absolute;top:213px;width:45px;height:45px;background:var(--white);display:flex;align-items:center;justify-content:center}
.slide-arrow.prev{left:82px}
.slide-arrow.next{left:1065px}
.slide-dots{position:absolute;top:440px;left:0;width:1200px;display:flex;justify-content:center;gap:4px;list-style:none}
.slide-dots li{width:8px;height:8px;background:var(--white)}
.slide-dots li.active{background:transparent;border:2px solid var(--white)}

.about{position:absolute;top:590px;left:0;width:1200px;height:410px}
.founders-photo{position:absolute;left:145px;top:58px;width:280px;height:352px;
  background:linear-gradient(180deg,var(--photo-light) 0%,var(--photo-mid) 50%,var(--photo-low) 100%)}
.section-title{position:absolute;top:78px;left:0;width:1200px;text-align:center;font-size:27px;line-height:36px;font-weight:400;letter-spacing:.5px;text-transform:uppercase}
.what-we-do{position:absolute;left:573px;top:193px;width:500px}
.what-we-do h3{font-size:21px;line-height:28px;font-weight:400;text-transform:uppercase;margin-bottom:6px}
.what-we-do p{font-family:"Open Sans",sans-serif;font-size:14.4px;line-height:25.6px;color:var(--body-text);letter-spacing:-.1px}
</style>
</head>
<body>
<header class="site-header">
  <div class="menu-toggle">
    <svg width="23" height="12" viewBox="0 0 23 12"><path d="M0 1h23M0 6h23M0 11h23" stroke="#222" stroke-width="1.5"/></svg>
    MENU
  </div>
  <div class="brand">Jest Harbor</div>
  <ul class="social">
    <li>Chirper</li><li>Friendbook</li><li>Pinboardly</li><li>Shotcase</li>
  </ul>
</header>

<section class="hero" role="img" aria-label="Photo of two comedians performing in front of a red stage curtain">
  <h1 class="hero-title"><strong>Your Team's</strong> Desk-Grin<br>Ratio</h1>
  <a class="slide-arrow prev" aria-label="Previous slide">
    <svg width="34" height="28" viewBox="0 0 34 28"><path d="M33 14H2M14 2L2 14l12 12" fill="none" stroke="#222" stroke-width="1.5"/></svg>
  </a>
  <a class="slide-arrow next" aria-label="Next slide">
    <svg width="34" height="28" viewBox="0 0 34 28"><path d="M1 14h31M20 2l12 12-12 12" fill="none" stroke="#222" stroke-width="1.5"/></svg>
  </a>
  <ul class="slide-dots"><li class="active"></li><li></li><li></li><li></li></ul>
</section>

<section class="about">
  <div class="founders-photo" role="img" aria-label="Portrait photo of the two Jest Harbor founders"></div>
  <h2 class="section-title">About Jest Harbor</h2>
  <div class="what-we-do">
    <h3>What We Do</h3>
    <p>Mauris a massa id leo aliquam consequat porttitor vitae est. Proin ultricies velit sed porttitor viverra. Pellen-tesque eget tristique est. Donec volutpat, eros et bibendum lacinia Lorem ipsum dolor sit amet, consectetur adipisic-ing elit.<br>&nbsp;sed do eiusmod tempor incididunt ut labore et dolore magna aliqua. Ut enim ad minim veniam, quis nostrud exercitation ullamco laboris nisi ut aliquip ex ea commodo consequat. Duis aute irure dolor in reprehenderit in</p>
  </div>
</section>
</body>
</html>
```